Cover Page for Pixelwall, Workbridge & Dwellora.com

I'm needing a cover page for Pixelwall, Workbridge & Dwellora.com. I already have my logo and some samples of what I'm looking for but open to new ideals. I'm in the real estate business and want something that looks very professional and clean. The area I cover is located in the Lake Norman area of North Carolina so would like to incorporate a lake background along with my logo, headshot and contact information.

```html
<!DOCTYPE html>
<html lang="en">
<head>
<meta charset="utf-8">
<title>Evan Halloway – Broker | Realtor Cover</title>
<link rel="stylesheet" href="https://fonts.googleapis.com/css2?family=Montserrat:wght@500;600&family=Open+Sans:wght@400;600&display=swap">
<style>
  :root {
    --sky-top: #5f8fbf;
    --sky-mid: #a9bfd0;
    --horizon: #e9b46a;
    --sun: #fff2c4;
    --shore: #2b2a28;
    --water: #9aa9b3;
    --water-deep: #6f8aa0;
    --suit: #4f6688;
    --white: #ffffff;
  }
  html, body {
    margin: 0;
    padding: 0;
    width: 1200px;
    height: 381px;
    overflow: hidden;
  }
  .cover {
    position: relative;
    width: 1200px;
    height: 381px;
    overflow: hidden;
    color: var(--white);
    font-family: "Open Sans", sans-serif;
  }
  .lake-scene {
    position: absolute;
    inset: 0;
    background:
      radial-gradient(ellipse 90px 60px at 636px 165px, var(--sun) 0%, rgba(255,214,140,0.7) 40%, rgba(233,180,106,0) 100%),
      radial-gradient(ellipse 40px 70px at 636px 255px, rgba(255,226,160,0.85) 0%, rgba(240,180,100,0) 100%),
      linear-gradient(to bottom,
        var(--sky-top) 0%,
        var(--sky-mid) 30%,
        #c9c3b4 44%,
        var(--horizon) 52%,
        var(--shore) 56%,
        #3f3a33 58%,
        #a58462 62%,
        var(--water) 78%,
        var(--water-deep) 100%);
  }
  .identity {
    position: absolute;
    left: 0;
    top: 0;
    width: 636px;
    text-align: center;
  }
  .agent-name {
    position: absolute;
    left: 0;
    width: 636px;
    top: 160px;
    margin: 0;
    font-family: "Montserrat", sans-serif;
    font-weight: 600;
    font-size: 50px;
    letter-spacing: 1px;
    line-height: 1;
  }
  .agent-title {
    position: absolute;
    left: 0;
    width: 636px;
    top: 220px;
    margin: 0;
    font-family: "Montserrat", sans-serif;
    font-weight: 500;
    font-size: 14px;
    letter-spacing: 7px;
  }
  .agent-title sup { font-size: 7px; letter-spacing: 0; }
  .phone {
    position: absolute;
    left: 150px;
    top: 256px;
    display: flex;
    align-items: center;
    gap: 12px;
    font-weight: 600;
    font-size: 33px;
    line-height: 1;
  }
  .phone svg { width: 42px; height: 38px; }
  .address {
    position: absolute;
    left: 0;
    width: 636px;
    top: 308px;
    margin: 0;
    font-size: 18px;
    line-height: 20px;
    font-style: normal;
  }
  .headshot {
    position: absolute;
    left: 569px;
    top: 24px;
    width: 393px;
    height: 357px;
    border-radius: 150px 150px 0 0;
    background:
      radial-gradient(ellipse 80px 110px at 197px 120px, #c99c86 0%, #a8806d 60%, rgba(120,100,90,0) 100%),
      linear-gradient(to bottom, rgba(60,50,45,0.2) 0%, var(--suit) 70%, #3e5272 100%);
  }
  .badge {
    position: absolute;
    border: 1.5px solid rgba(255,255,255,0.85);
    background: rgba(255,255,255,0.12);
  }
  .badge-luxury { left: 912px; top: 114px; width: 210px; height: 72px; border-radius: 36px; }
  .badge-leading { left: 918px; top: 198px; width: 200px; height: 78px; border-radius: 6px; }
</style>
</head>
<body>
  <main class="cover">
    <div class="lake-scene" role="img" aria-label="Sunset over a calm lake with a tree-lined shore and reflections on the water"></div>

    <section class="identity">
      <h1 class="agent-name">EVAN HALLOWAY</h1>
      <p class="agent-title">BROKER | REALTOR<sup>®</sup></p>
      <div class="phone">
        <svg viewBox="0 0 42 38" fill="none" stroke="currentColor" stroke-width="1.6" stroke-linecap="round" aria-hidden="true">
          <rect x="14" y="3" width="14" height="30" rx="3" transform="rotate(-18 21 18)"/>
          <path d="M8 12 q-4 6 0 12 M4 9 q-6 9 0 18 M34 11 q4 6 0 12 M38 8 q6 9 0 18"/>
        </svg>
        <span>(555) 013-2748</span>
      </div>
      <address class="address">
        Lakeside Sales, 418 Shoreline Drive<br>
        Mailing PO Box 2210, Harbor Point, NC 28000
      </address>
    </section>

    <div class="headshot" role="img" aria-label="Headshot of the agent in a blue plaid blazer and white shirt"></div>

    <div class="badge badge-luxury" role="img" aria-label="Luxury real estate network badge"></div>
    <div class="badge badge-leading" role="img" aria-label="Global real estate companies network badge"></div>
  </main>
</body>
</html>
```